Fresh Start Body Quest 2017 Poster

We are having a Fresh Start, Body Quest for 2017 at our fitness studio. We need a poster design using the template attached as a reference (Only reference). I have also included our Drovelux logo to put on the poster. Please DO NOT use the graphics in the flyer as we are expecting something much much better :-)
MUST HAVES:
- Size needed 11x17 with bleeding for printing
- .PSD File Format WITH LAYERS (CS3 Compatible)*** A MUST
- Use Drovelux Bootcamps Logo
- Use Information in the attached word doc

```html
<!DOCTYPE html>
<html lang="en">
<head>
<meta charset="UTF-8">
<title>Drovelux Bootcamps – Fresh Start Body Quest 2017</title>
<link href="https://fonts.googleapis.com/css2?family=Staatliches&family=Gochi+Hand&family=Oswald:wght@500;700&display=swap" rel="stylesheet">
<style>
  :root{
    --bg:#b9b9b9;
    --paper:#f3f3f2;
    --paper-shade:#e2e2e0;
    --ink:#222222;
    --navy:#1f2a44;
    --blue:#3f86cc;
    --orange:#c87a2a;
    --orange-light:#e49a45;
    --white:#ffffff;
  }
  *{box-sizing:border-box;margin:0;padding:0}
  html,body{width:1200px;height:1200px;overflow:hidden;background:var(--bg)}
  .poster{
    position:absolute;left:224px;top:20px;width:752px;height:1160px;
    background:radial-gradient(ellipse at 40% 45%, var(--paper) 55%, var(--paper-shade) 100%);
    box-shadow:0 8px 24px rgba(0,0,0,.25);
    overflow:hidden;
  }
  .abs{position:absolute}
  .center{text-align:center;transform:translateX(-50%);white-space:nowrap}
  .ribbon{left:59px;top:0;width:151px;height:251px}
  .ribbon-text{
    left:134px;top:22px;font-family:'Oswald',sans-serif;font-weight:700;
    color:var(--white);font-size:34px;line-height:39px;text-align:center;
    transform:translateX(-50%)
  }
  .brand{
    left:239px;top:51px;width:466px;height:153px;
    display:flex;align-items:center;justify-content:center;gap:16px;
  }
  .brand-mark{width:20px;height:20px;border-radius:50%;background:var(--ink);flex:none}
  .brand-name{font-family:'Staatliches',sans-serif;font-size:58px;color:var(--ink);line-height:.95}
  .headline{font-family:'Staatliches',sans-serif;text-transform:uppercase;line-height:1}
  .headline--orange{color:var(--orange);font-size:50px}
  .headline--dark{color:var(--ink);font-size:49px}
  .badge{left:63px;top:277px;width:146px;height:146px}
  .badge-text{left:136px;top:300px;color:var(--white);font-family:'Oswald',sans-serif;text-align:center;transform:translateX(-50%) rotate(-4deg)}
  .badge-small{font-style:italic;font-weight:500;font-size:24px;line-height:26px}
  .badge-big{font-weight:700;font-size:40px;line-height:40px}
  .script{font-family:'Gochi Hand',cursive;color:var(--blue);font-size:38px;line-height:1}
  .hand{font-family:'Gochi Hand',cursive;color:var(--ink);font-size:30px;line-height:1;font-weight:700}
  .hand sup{font-size:.55em}
  .dates-frame{left:40px;top:571px;width:684px;height:104px}
  .finale{color:var(--orange);font-family:'Staatliches',sans-serif;font-size:48px;text-transform:uppercase;line-height:1}
  .finale sup{font-size:.5em}
  .offer-frame{left:58px;top:772px;width:630px;height:117px}
  .offer{font-family:'Staatliches',sans-serif;color:var(--ink);font-size:42px;line-height:44px;text-transform:uppercase}
  .prize{
    left:38px;top:917px;width:683px;height:86px;border-radius:10px;
    background:linear-gradient(180deg,var(--orange-light),var(--orange));
    display:flex;align-items:center;justify-content:center;
    font-family:'Oswald',sans-serif;font-weight:700;font-size:48px;color:var(--white)
  }
  .contact{font-family:'Oswald',sans-serif;color:var(--navy);line-height:1;font-weight:700}
  .contact--label{font-size:30px;font-weight:500}
  .contact--url{font-size:33px}
</style>
</head>
<body>
<main class="poster">

  <svg class="abs ribbon" viewBox="0 0 151 251" aria-hidden="true">
    <polygon points="0,0 151,0 151,251 75,215 0,251" fill="var(--orange)"/>
    <polygon points="12,0 139,0 139,228 75,198 12,228" fill="var(--blue)"/>
    <polyline points="18,0 18,220 75,192 133,220 133,0" fill="none" stroke="#fff" stroke-width="1.5" stroke-dasharray="3 3"/>
  </svg>
  <div class="abs ribbon-text">FRESH<br>START<br>BODY<br>QUEST</div>

  <div class="abs brand">
    <span class="brand-mark"></span>
    <span class="brand-name">DROVELUX<br>BOOTCAMPS</span>
  </div>

  <svg class="abs badge" viewBox="0 0 146 146" aria-hidden="true">
    <circle cx="73" cy="73" r="71" fill="var(--ink)"/>
    <circle cx="75" cy="71" r="65" fill="var(--orange)"/>
  </svg>
  <div class="abs badge-text">
    <div class="badge-small">in just</div>
    <div class="badge-big">SIX</div>
    <div class="badge-small">WEEKS</div>
  </div>

  <h1 class="abs center headline headline--orange" style="left:452px;top:258px">Transform Your Body &amp;</h1>
  <p class="abs center headline headline--dark" style="left:445px;top:314px">Get in the Best</p>
  <p class="abs center headline headline--dark" style="left:448px;top:366px">Shape of Your Life!</p>

  <p class="abs center script" style="left:385px;top:455px">Kick Off Meeting:</p>
  <p class="abs center hand" style="left:385px;top:500px">Thursday, Jan 12<sup>th</sup> at 7:30 pm</p>

  <svg class="abs dates-frame" viewBox="0 0 684 104" aria-hidden="true">
    <path d="M2,4 L336,3 M350,3 L682,5" stroke="var(--ink)" stroke-width="5" fill="none"/>
    <path d="M3,4 L2,50 M681,5 L682,40" stroke="var(--ink)" stroke-width="2" fill="none"/>
  </svg>
  <p class="abs center script" style="left:200px;top:596px">Start Date:</p>
  <p class="abs center hand" style="left:200px;top:638px">Tuesday, January 17<sup>th</sup></p>
  <p class="abs center script" style="left:547px;top:596px">End Date:</p>
  <p class="abs center hand" style="left:547px;top:638px">Saturday, February 25<sup>th</sup></p>

  <p class="abs center finale" style="left:368px;top:697px">Finale Party March 2<sup>nd</sup></p>

  <svg class="abs offer-frame" viewBox="0 0 630 117" aria-hidden="true">
    <path d="M290,3 L628,2 L626,60 M2,50 L3,114 L340,112" stroke="var(--blue)" stroke-width="4" fill="none"/>
  </svg>
  <div class="abs center offer" style="left:368px;top:790px">6 Weeks of Training, Nutrition,<br>Starting at just $99!</div>

  <div class="abs prize">$500 CASH Prize for Winner!</div>

  <p class="abs center contact contact--label" style="left:374px;top:1026px">VISIT</p>
  <p class="abs center contact contact--url" style="left:374px;top:1064px">www.droveluxbootcamps.com</p>
  <p class="abs center contact contact--label" style="left:374px;top:1102px">FOR MORE INFO</p>

</main>
</body>
</html>
```